Business card - Brio Margin - size 85 mm * 55 mm

We need new business cards. Design must fit with our vision of the firm. You find in the attached file our logo and a short description of our firm (mission, vision, value, business and so on).

Target Market(s)

Consulting firm in performance improvement

Industry/Entity Type

Management Consulting

Contact Information for Business Card

SIZE
85 mm * 55 mm
INFORMATIONS
name surname
role position
telephone number
email address

Requirements
Must have
• the brand must APPEAR for the rest Would we like to have something sleek, inspired to a "just right" approach
Should not have
• Please avoid the black color as background

```html
<!DOCTYPE html>
<html lang="en">
<head>
<meta charset="utf-8">
<title>Brio Margin – Business Card</title>
<link rel="stylesheet" href="https://fonts.googleapis.com/css2?family=Roboto:wght@400;500;700&display=swap">
<style>
  :root {
    --bg: #e4e4e4;
    --card: #ffffff;
    --orange: #e8731f;
    --orange-light: #f19a3a;
    --orange-deep: #d9501a;
    --green: #6cb52d;
    --ink: #4a4a4a;
    --ink-soft: #6b6b6b;
  }
  * { box-sizing: border-box; margin: 0; padding: 0; }
  html, body {
    width: 1200px; height: 852px; overflow: hidden;
    background: var(--bg);
    font-family: "Roboto", Arial, sans-serif;
  }
  .stage { position: relative; width: 1200px; height: 852px; }

  .card {
    position: absolute;
    width: 540px; height: 350px;
    background: var(--card);
    border-radius: 16px;
    overflow: hidden;
    box-shadow: 0 6px 18px rgba(0,0,0,0.18);
  }
  .card--front { left: 40px; top: 110px; border-bottom: 8px solid var(--orange); }
  .card--back  { left: 620px; top: 390px; }

  .brand {
    position: absolute;
    display: flex; flex-direction: column; align-items: center; gap: 16px;
  }
  .brand__dot {
    width: 74px; height: 74px; border-radius: 50%;
    border: 4px solid var(--orange);
  }
  .brand__name {
    color: var(--orange);
    font-weight: 500;
    font-size: 20px;
    letter-spacing: 0.42em;
    white-space: nowrap;
  }
  .card--front .brand { left: 0; right: 0; top: 100px; }
  .card--back .brand { left: 40px; top: 110px; }
  .card--back .brand__name { font-size: 17px; }

  .wave { position: absolute; inset: 0; width: 100%; height: 100%; }

  .person {
    position: absolute; right: 34px; top: 34px; text-align: right;
  }
  .person__name { color: var(--ink); font-weight: 700; font-size: 22px; }
  .person__role { color: var(--ink-soft); font-size: 12px; margin-top: 2px; }

  .contact {
    position: absolute; right: 26px; bottom: 40px;
    list-style: none; text-align: right;
    color: #fff; font-size: 13.5px; line-height: 21px;
  }
  .contact li { display: flex; justify-content: flex-end; align-items: center; gap: 8px; }
  .contact svg { width: 13px; height: 13px; fill: #fff; }
  .contact .no-icon { padding-right: 21px; }
</style>
</head>
<body>
<main class="stage">

  <section class="card card--front" aria-label="Card front">
    <div class="brand">
      <span class="brand__dot"></span>
      <span class="brand__name">BRIO MARGIN</span>
    </div>
  </section>

  <section class="card card--back" aria-label="Card back">
    <svg class="wave" viewBox="0 0 540 350" preserveAspectRatio="none" aria-hidden="true">
      <defs>
        <linearGradient id="orangeFill" x1="0" y1="1" x2="1" y2="0">
          <stop offset="0" stop-color="#d9501a"/>
          <stop offset="0.55" stop-color="#e8731f"/>
          <stop offset="1" stop-color="#f3a23e"/>
        </linearGradient>
      </defs>
      <path d="M0,300 C170,292 300,240 380,160 C430,110 480,72 540,62
               L540,74 C485,86 440,122 392,172 C310,258 180,312 0,318 Z"
            fill="var(--green)"/>
      <path d="M0,326 C190,318 320,250 400,165 C450,115 495,95 540,90 L540,350 L0,350 Z"
            fill="url(#orangeFill)"/>
    </svg>

    <div class="brand">
      <span class="brand__dot"></span>
      <span class="brand__name">BRIO MARGIN</span>
    </div>

    <div class="person">
      <p class="person__name">Mara Ellison</p>
      <p class="person__role">Managing Director</p>
    </div>

    <ul class="contact">
      <li>+1 555 014 2270
        <svg viewBox="0 0 24 24" aria-hidden="true"><path d="M6.6 10.8a15 15 0 0 0 6.6 6.6l2.2-2.2c.3-.3.7-.4 1-.2 1.1.4 2.3.6 3.6.6.6 0 1 .4 1 1V20c0 .6-.4 1-1 1C10.6 21 3 13.4 3 4c0-.6.4-1 1-1h3.5c.6 0 1 .4 1 1 0 1.3.2 2.5.6 3.6.1.3 0 .7-.2 1z"/></svg>
      </li>
      <li>www.briomargin.com
        <svg viewBox="0 0 24 24" aria-hidden="true"><path d="M12 2a10 10 0 1 0 0 20 10 10 0 0 0 0-20zm6.9 6h-3a15 15 0 0 0-1.3-3.9A8 8 0 0 1 18.9 8zM12 4c.8 1.2 1.5 2.5 1.9 4h-3.8c.4-1.5 1.1-2.8 1.9-4zM4.3 14a8 8 0 0 1 0-4h3.4a16 16 0 0 0 0 4zm.8 2h3a15 15 0 0 0 1.3 3.9A8 8 0 0 1 5.1 16zm3-8h-3a8 8 0 0 1 4.3-3.9C8.8 5.3 8.4 6.6 8.1 8zM12 20c-.8-1.2-1.5-2.5-1.9-4h3.8c-.4 1.5-1.1 2.8-1.9 4zm2.3-6H9.7a14 14 0 0 1 0-4h4.6a14 14 0 0 1 0 4zm.3 5.9c.6-1.2 1-2.5 1.3-3.9h3a8 8 0 0 1-4.3 3.9zm1.7-5.9a16 16 0 0 0 0-4h3.4a8 8 0 0 1 0 4z"/></svg>
      </li>
      <li>mara@briomargin.com
        <svg viewBox="0 0 24 24" aria-hidden="true"><path d="M3 5h18c.6 0 1 .4 1 1v12c0 .6-.4 1-1 1H3c-.6 0-1-.4-1-1V6c0-.6.4-1 1-1zm9 7.2L4.6 7H4v.6l8 5.6 8-5.6V7h-.6z"/></svg>
      </li>
      <li class="no-icon">410 Alder Lane Suite 8 Corvallis Oregon 97330</li>
    </ul>
  </section>

</main>
</body>
</html>
```